Walk Bright through the Seasons: 52 Weeks to a Year of Courage and Calm

This is a non-fiction, self-help book. The first edition was published a decade ago, and it needs a new design. Nothing too literal (no actual hearts on the cover) but something inspirational or perhaps something quite plain. The current cover is below for reference, but I DO NOT want something similar to that. It is outdated.

The cover must include:

1. Title: Walk Bright through the Seasons
2. Subtitle: 52 Weeks to a Year of Courage and Calm
3. Author Name: Tobin Wells

It should also have plenty of "white space" in other words the fonts shouldnt be so big that they take up the whole cover.

Dimensions: 9" x 6.25"

Target Market(s)

adults interested in personal development

Font styles to use
Serif
Script

Colors

Designer to choose colors to be used in the design.

Requirements
Must have
• Classic look and feel. The current design is too busy. I have included examples of the style I like below. I'm open to a singular graphic/photo but nothing more than that. Probably plain text is best.
• Please look at the samples I have included of best-selling books in the genre that I like. The cover should be modeled after these.

```html
<!DOCTYPE html>
<html lang="en">
<head>
<meta charset="utf-8">
<title>Walk Bright through the Seasons — Tobin Wells</title>
<link rel="stylesheet" href="https://fonts.googleapis.com/css2?family=Cormorant+Garamond:ital,wght@0,500;0,600;1,500&family=Pinyon+Script&display=swap">
<style>
  :root {
    --stage: #1c1e20;
    --cover-ivory: #f4efe4;
    --cover-ivory-edge: #ebe4d4;
    --ink-teal: #1f4f55;
    --accent-gold: #b38a4a;
    --ink-soft: #4a5a5c;
  }
  * { box-sizing: border-box; margin: 0; padding: 0; }
  html, body {
    width: 1200px;
    height: 870px;
    overflow: hidden;
    background: var(--stage);
  }
  .stage {
    width: 1200px;
    height: 870px;
    display: flex;
    align-items: center;
    justify-content: center;
  }
  .book-cover {
    position: relative;
    width: 556px;
    height: 800px;
    background: radial-gradient(ellipse at 50% 40%, var(--cover-ivory) 0%, var(--cover-ivory-edge) 100%);
    display: flex;
    flex-direction: column;
    align-items: center;
    text-align: center;
    padding: 170px 60px 90px;
  }
  .title-block {
    color: var(--ink-teal);
    font-weight: 500;
    display: flex;
    flex-direction: column;
    align-items: center;
  }
  .title-serif {
    font-family: "Cormorant Garamond", serif;
    font-weight: 500;
    text-transform: uppercase;
    line-height: 1;
  }
  .title-top {
    font-size: 42px;
    letter-spacing: 0.14em;
    padding-left: 0.14em;
  }
  .title-script {
    font-family: "Pinyon Script", cursive;
    font-size: 44px;
    line-height: 1;
    color: var(--accent-gold);
    margin: 14px 0 10px;
  }
  .title-bottom {
    font-size: 56px;
    letter-spacing: 0.16em;
    padding-left: 0.16em;
  }
  .divider {
    width: 64px;
    height: 1px;
    background: var(--accent-gold);
    margin: 40px 0 26px;
  }
  .subtitle {
    font-family: "Cormorant Garamond", serif;
    font-style: italic;
    font-weight: 500;
    font-size: 20px;
    line-height: 1.4;
    color: var(--ink-soft);
  }
  .author {
    margin-top: auto;
    font-family: "Cormorant Garamond", serif;
    font-weight: 600;
    font-size: 20px;
    letter-spacing: 0.28em;
    padding-left: 0.28em;
    text-transform: uppercase;
    color: var(--ink-teal);
  }
</style>
</head>
<body>
  <main class="stage">
    <section class="book-cover" aria-label="Book cover">
      <h1 class="title-block">
        <span class="title-serif title-top">Walk Bright</span>
        <span class="title-script">through the</span>
        <span class="title-serif title-bottom">Seasons</span>
      </h1>
      <span class="divider" aria-hidden="true"></span>
      <p class="subtitle">52 Weeks to a Year of Courage and Calm</p>
      <p class="author">Tobin Wells</p>
    </section>
  </main>
</body>
</html>
```